THE GRAND DELTA GROOVE REVUE---a CONCERT

We need a web page to support our upcoming concert asap. It is a southern blues concert featuring Odessa Brantley, Whitfield, Marvell Gaddis, and Reuben Oakes. We have as special guest local talent from the Augusta, Ga Area---Calloway, Abe Lark and Jo'Vanna. Hosted By: Augusta's Own--Brave Pecan.
The concert is as follow:
The Grand Delta Groove Revue
Saturday, July 7, 2018
7:00 pm Doors open at 6:00pm
Harlow Civic Hall, Augusta, GA
Tickets are $39, $49 and $59
Tickets on sale at the Box Office(need link to "BUY TICKETS"), Zenith Records, Marigold Box Office and Camp Hollister, GA
We are honoring all military and first responders and offering discount tickets--contact 770-555-0182 for discount code
Overnight concert guests are invited to stay at the Restwell Lodge in Augusta for a reduced rate of $69--we would like a link to that site. Mention Code:
The Concert is promoted by QUARTZ MERIDIAN ENTERTAINMENT
The Harlow Civic Hall Logo and Adress must appear somewhere at the bottom or near where the Harlow Civic Hall is mentioned.
The Military requires that we say, No government or military endorsement implied.
Picture of the Artists and our current flyer is attached. If you need the layered file--contact us

Target Market(s)

blues music lovers and concert goers

Requirements
Must have
• link to buy tickets/mention chatterly and peepline
Nice to have
• links to artist sites and hotel, TICKET GIVEAWAY REGISTRATION

```html
<!DOCTYPE html>
<html lang="en">
<head>
<meta charset="utf-8">
<title>The Grand Delta Groove Revue</title>
<link rel="stylesheet" href="https://fonts.googleapis.com/css2?family=Roboto:wght@300;400;500;700&family=Playfair+Display:wght@400;700&display=swap">
<style>
:root{
  --ink:#ffffff;
  --muted:#d6d6d6;
  --gold:#f0c060;
  --orange:#ff6a00;
  --orange-light:#ffa24a;
  --red:#e8200a;
  --dark:#232323;
  --darker:#141414;
  --black:#000000;
  --ring:#f08a2a;
}
*{margin:0;padding:0;box-sizing:border-box}
html,body{width:1200px;height:2557px;overflow:hidden;background:var(--black)}
body{position:relative;font-family:"Roboto",Arial,sans-serif;color:var(--ink)}
a{color:inherit;text-decoration:none}
.abs{position:absolute}

/* hero */
.hero{left:0;top:0;width:1200px;height:690px;
  background:radial-gradient(ellipse at 50% 20%,#b2341c 0%,#6a160c 35%,#2a0806 65%,#000 100%)}
.hero-crowd{left:0;top:420px;width:1200px;height:270px;
  background:linear-gradient(180deg,rgba(0,0,0,0) 0%,rgba(0,0,0,.85) 60%,#000 100%)}
.brand{left:183px;top:26px;line-height:1}
.brand .top{font-size:28px;font-weight:400;letter-spacing:.5px}
.brand .bottom{font-size:30px;font-weight:700;margin-top:2px}
.nav{left:510px;top:44px;display:flex;gap:24px;font-size:13px;font-weight:500;text-transform:uppercase}
.nav a{color:var(--muted)}
.nav a.active{color:var(--ink)}
.event-title{left:0;top:200px;width:1200px;text-align:center;font-family:"Playfair Display",Georgia,serif;color:var(--gold);line-height:1.05}
.event-title .small{font-size:30px;font-style:normal}
.event-title .big{font-size:62px;font-weight:700;letter-spacing:2px}
.event-title .sub{font-size:30px}
.when{left:0;top:366px;width:1200px;text-align:center;font-family:"Playfair Display",Georgia,serif;line-height:1.2}
.when .date{font-size:29px;color:var(--gold)}
.when .time{font-size:29px}
.when .place{font-size:33px}
.disclaimer{left:0;top:487px;width:1200px;text-align:center;font-size:15px}

/* listen band */
.listen{left:0;top:690px;width:1200px;height:65px;background:linear-gradient(90deg,var(--orange) 0%,var(--orange-light) 100%)}
.listen-tab{left:0;top:690px;width:420px;height:65px;background:linear-gradient(180deg,#ff5010,var(--red));clip-path:polygon(0 0,100% 0,365px 100%,0 100%)}
.listen-label{left:236px;top:710px;font-size:21px;font-weight:500}
.listen-track{left:446px;top:710px;display:flex;align-items:center;gap:12px;font-size:16px;font-weight:500}

/* about */
.about{left:0;top:755px;width:1200px;height:470px;background:var(--dark)}
.portrait-frame{left:157px;top:782px;width:386px;height:386px;border-radius:50%;background:#4a4a4a}
.portrait{left:165px;top:790px;width:370px;height:370px;border-radius:50%;
  background:radial-gradient(circle at 50% 35%,#6fd0f0 0%,#2aa4d8 45%,#5a2a18 75%,#3a1a10 100%)}
.about-copy{left:580px;top:820px;width:480px}
.about-copy h2{font-size:25px;font-weight:500;line-height:1.25;margin-bottom:18px}
.about-copy p{font-size:16px;line-height:1.6;color:var(--muted);margin-bottom:6px}
.btn-outline{display:inline-block;border:2px solid var(--ring);color:var(--orange-light);font-size:14px;padding:9px 30px;margin-top:28px}

/* tickets */
.tickets{left:0;top:1190px;width:1200px;height:523px;
  background:radial-gradient(ellipse at 70% 60%,#555 0%,#2e2e2e 50%,#161616 100%)}
.tickets-curve{left:0;top:1180px;width:1200px;height:80px}
.tickets h2{left:0;top:1238px;width:1200px;text-align:center;font-size:31px;font-weight:400}
.price{width:214px;height:214px;border:3px solid var(--ring);border-radius:50%;background:rgba(0,0,0,.35);display:flex;flex-direction:column;align-items:center;justify-content:center;top:1296px}
.price .amount{font-size:46px;font-weight:300;margin-bottom:14px}
.price .buy{border:2px solid var(--ring);color:var(--orange-light);font-size:11px;font-weight:500;padding:6px 12px}
.tickets-note{left:0;top:1572px;width:1200px;text-align:center;font-size:17px;line-height:1.5}
.tickets-note .second{font-size:18px;margin-top:8px}

/* giveaway */
.giveaway{left:0;top:1713px;width:1200px;height:480px;background:var(--orange)}
.giveaway-photo{left:0;top:1713px;width:1200px;height:480px;
  clip-path:polygon(750px 0,1200px 0,1200px 480px,510px 480px);
  background:radial-gradient(ellipse at 65% 30%,#fff8d0 0%,#e8c040 18%,#6a8a30 40%,#1a3a20 65%,#0a0a0a 100%)}
.giveaway-form{left:181px;top:1798px;width:460px}
.giveaway-form h2{font-size:33px;font-weight:400;margin-bottom:12px}
.giveaway-form p{font-size:14px;line-height:1.6;margin-bottom:22px}
.field{width:316px;height:36px;background:#fff;color:#333;font-size:14px;padding:9px 16px;margin-bottom:6px}
.btn-light{display:inline-block;border:2px solid #fff;font-size:14px;padding:9px 36px;margin-top:12px}

/* hotel */
.hotel{left:0;top:2193px;width:1200px;height:177px;background:var(--dark)}
.hotel-mark{left:253px;top:2233px;width:86px;height:100px;background:#6e1224}
.hotel-name{left:253px;top:2340px;font-size:13px;font-weight:500}
.hotel-copy{left:378px;top:2250px;width:620px;font-size:21px;line-height:1.4}

/* footer */
.footer{left:0;top:2370px;width:1200px;height:187px;background:var(--black)}
.copyright{left:170px;top:2406px;font-size:14px;color:#9a9a9a}
.social{left:170px;top:2446px;display:flex;gap:16px;font-size:13px}
.social a{display:flex;align-items:center;gap:6px}
.social .dot{width:30px;height:30px;border:2px solid #fff;border-radius:50%}
.venue{left:565px;top:2410px;display:flex;align-items:center;gap:18px}
.venue .badge{width:100px;height:60px;border-radius:50%;background:#2a5a9a}
.venue .name{font-family:"Playfair Display",Georgia,serif;font-size:30px;color:var(--gold);letter-spacing:2px}
.address{left:568px;top:2470px;display:flex;align-items:center;gap:6px;font-size:16px}
</style>
</head>
<body>

<section class="hero abs" role="img" aria-label="Concert stage with red lights and a cheering crowd"></section>
<div class="hero-crowd abs"></div>

<a class="brand abs" href="#">
  <div class="top">DELTA GROOVE</div>
  <div class="bottom">REVUE CONCERT</div>
</a>
<nav class="nav abs">
  <a class="active" href="#">Home</a>
  <a href="#">About</a>
  <a href="#">Our Concert</a>
  <a href="#">Book Ticket</a>
  <a href="#">Artists</a>
  <a href="#">Contact</a>
</nav>

<h1 class="event-title abs">
  <div class="small">The Grand</div>
  <div class="big">DELTA GROOVE</div>
  <div class="sub">REVUE</div>
</h1>
<div class="when abs">
  <div class="date">SATURDAY, JULY 7, 2018</div>
  <div class="time">7:00 PM DOORS OPEN AT 6:00PM</div>
  <div class="place">HARLOW CIVIC HALL, AUGUSTA, GA</div>
</div>
<p class="disclaimer abs">The Military requires that we say, No government or military endorsement implied</p>

<div class="listen abs"></div>
<div class="listen-tab abs"></div>
<div class="listen-label abs">LISTEN NOW</div>
<div class="listen-track abs">
  <svg width="18" height="20" viewBox="0 0 18 20"><polygon points="0,0 18,10 0,20" fill="#fff"/></svg>
  <span>THE GRAND GROOVE 30 SEC FRIDAY</span>
  <svg width="22" height="20" viewBox="0 0 22 20"><polygon points="0,6 5,6 11,1 11,19 5,14 0,14" fill="#fff"/><path d="M14 6 Q17 10 14 14 M16 3 Q21 10 16 17" stroke="#fff" stroke-width="2" fill="none"/></svg>
</div>

<section class="about abs"></section>
<div class="portrait-frame abs"></div>
<div class="portrait abs" role="img" aria-label="Portrait of a featured blues artist"></div>
<div class="about-copy abs">
  <h2>THE CONCERT IS PROMOTED<br>BY QUARTZ MERIDIAN ENTERTAINMENT</h2>
  <p>We have as special guest local talent from the Augusta, Ga Area---Calloway, Abe Lark and Jo'Vanna. Hosted By: Augusta's Own--Brave Pecan.</p>
  <p>It is a southern blues concert featuring Odessa Brantley, Whitfield, Marvell Gaddis, and Reuben Oakes.</p>
  <a class="btn-outline" href="#">BOOK NOW</a>
</div>

<section class="tickets abs" role="img" aria-label="Black and white crowd with raised hands"></section>
<svg class="tickets-curve abs" viewBox="0 0 1200 80" preserveAspectRatio="none"><path d="M0 0 H1200 V80 Q600 -20 0 60 Z" fill="#232323"/></svg>
<h2 class="abs" style="left:0;top:1238px;width:1200px;text-align:center;font-size:31px;font-weight:400">TICKET</h2>
<div class="price abs" style="left:259px"><div class="amount">$39</div><a class="buy" href="#">BUY TICKETS</a></div>
<div class="price abs" style="left:495px"><div class="amount">$49</div><a class="buy" href="#">BUY TICKETS</a></div>
<div class="price abs" style="left:730px"><div class="amount">$59</div><a class="buy" href="#">BUY TICKETS</a></div>
<div class="tickets-note abs">
  <p>Tickets on sale at the Box Office, Zenith Records, Marigold Box Office and Camp Hollister, GA</p>
  <p class="second">We are honoring all military and first responders and offering discount<br>tickets--contact 770-555-0182 for discount code</p>
</div>

<section class="giveaway abs"></section>
<div class="giveaway-photo abs" role="img" aria-label="Concert crowd under bright stage lights and confetti"></div>
<form class="giveaway-form abs">
  <h2>TICKET GIVE AWAY</h2>
  <p>vn ullamcorper est eget tempor cursus neque mi consectetuer mi a ultricies massa est sed nisl Class aptent tac</p>
  <div class="field">Phone</div>
  <div class="field">Email address</div>
  <a class="btn-light" href="#">CLICK HERE</a>
</form>

<section class="hotel abs"></section>
<div class="hotel-mark abs"></div>
<div class="hotel-copy abs">Overnight concert guests are invited to stay at the <a href="#">Restwell Lodge</a> in Augusta for a reduced rate of $69</div>

<footer class="footer abs"></footer>
<p class="copyright abs">© 2018 Company Name &nbsp;All right reserved</p>
<div class="social abs">
  <a href="#"><span class="dot"></span>peepline</a>
  <a href="#"><span class="dot"></span>chatterly</a>
</div>
<div class="venue abs">
  <span class="badge"></span>
  <span class="name">HARLOW CIVIC HALL</span>
</div>
<div class="address abs">
  <svg width="12" height="18" viewBox="0 0 12 18"><path d="M6 0 A6 6 0 0 1 12 6 C12 10 6 18 6 18 C6 18 0 10 0 6 A6 6 0 0 1 6 0 Z" fill="#f0a020"/><circle cx="6" cy="6" r="2.2" fill="#000"/></svg>
  <span>480 Linden Row, Augusta, GA 30901</span>
</div>

</body>
</html>
```